specialised legal consultancy business needs an update on logo and office stationary.

Update on Logo - see attached.

update on email signature - something new and fresh with only the following details -

(the logo)
Advocate Karel Steenkamp
KS Venture Frameworks (Pty) Ltd (Reg No.: 2019 / 374915 / 07)
LLB, LLM (Cum Laude), Cert.Dir (ABNQE), FCG (PTVRO)
+27 82 596 1174
karel#veldanvik.com

Update on letterhead - something new and fresh and please more user-friendly. With the same details as per the email signature.

```html
<!DOCTYPE html>
<html lang="en">
<head>
<meta charset="utf-8">
<title>KS Venture Letterhead</title>
<link href="https://fonts.googleapis.com/css2?family=Montserrat:wght@500;600;700&family=Source+Sans+3:wght@400&family=Pinyon+Script&display=swap" rel="stylesheet">
<style>
  :root {
    --brand-blue: #2385aa;
    --brand-navy: #0d4a6e;
    --ink: #333333;
    --band-dark: #666666;
    --band-light: #dcdcde;
    --paper: #ffffff;
  }
  html, body { margin: 0; padding: 0; overflow: hidden; background: var(--paper); }
  .letterhead {
    position: relative; width: 855px; height: 1200px; overflow: hidden;
    background: var(--paper); color: var(--ink);
    font-family: "Source Sans 3", sans-serif;
  }
  .brand {
    position: absolute; left: 126px; top: 212px;
    display: flex; align-items: center; gap: 10px;
  }
  .brand-square { width: 18px; height: 18px; background: var(--brand-blue); }
  .brand-name {
    font-family: "Montserrat", sans-serif; font-weight: 700;
    font-size: 24px; letter-spacing: 3px; color: var(--ink); line-height: 1;
  }
  .contact {
    position: absolute; left: 588px; top: 100px;
    font-family: "Montserrat", sans-serif; font-weight: 500; font-size: 14.5px; color: var(--ink);
  }
  .contact-row { display: flex; align-items: center; gap: 14px; height: 20px; margin-bottom: 11px; }
  .contact-row svg { width: 16px; height: 14px; flex: none; }
  .recipient { position: absolute; left: 127px; top: 284px; }
  .recipient-label {
    font-family: "Montserrat", sans-serif; font-weight: 500;
    font-size: 14px; letter-spacing: 2.5px; margin: 0 0 5px 1px;
  }
  .recipient-name {
    font-family: "Montserrat", sans-serif; font-weight: 500;
    font-size: 13px; color: var(--brand-blue); margin: 0 0 6px;
  }
  .recipient-address { font-size: 10px; line-height: 16.8px; margin: 0 0 0 1px; }
  .letter-body {
    position: absolute; left: 126px; top: 428px; width: 603px;
    font-size: 10.6px; line-height: 13.4px; text-align: justify;
  }
  .letter-body p { margin: 0 0 13.4px; }
  .sign-off { position: absolute; left: 125px; top: 922px; font-size: 10.6px; line-height: 13.6px; }
  .sign-name {
    font-family: "Pinyon Script", cursive; font-size: 22px; color: var(--brand-blue);
    line-height: 1; margin: 0 0 6px;
  }
  .sign-details { margin: 0; }
  .footer-bands { position: absolute; left: 0; top: 1130px; width: 855px; height: 70px; }
</style>
</head>
<body>
<main class="letterhead">
  <header>
    <div class="brand">
      <span class="brand-square"></span>
      <span class="brand-name">KS VENTURE</span>
    </div>
    <div class="contact">
      <div class="contact-row">
        <svg viewBox="0 0 16 14" aria-hidden="true"><path fill="var(--brand-blue)" d="M1 5c0-3 14-3 14 0v1.5h-3.5V5h-7v1.5H1z M4 7h8l2 6H2z"/></svg>
        <span>+27 82 596 1174</span>
      </div>
      <div class="contact-row">
        <svg viewBox="0 0 16 14" aria-hidden="true"><rect x="0.5" y="1.5" width="15" height="11" fill="none" stroke="var(--brand-blue)" stroke-width="1.2"/><path d="M0.5 1.5l7.5 6 7.5-6M0.5 12.5l5.5-5M15.5 12.5l-5.5-5" fill="none" stroke="var(--brand-blue)" stroke-width="1.2"/></svg>
        <span>karel@veldanvik.com</span>
      </div>
    </div>
  </header>

  <section class="recipient">
    <p class="recipient-label">TO</p>
    <p class="recipient-name">Thomas Alan Reid</p>
    <p class="recipient-address">Human Resources<br>Corvale Inc.<br>4512 W&nbsp; Baltimore MD<br>USA</p>
  </section>

  <article class="letter-body">
    <p>Lorem ipsum dolor sit amet, consectetuer adipiscing elit, sed diam nonmmy nibh euismod tincidunt ut laoreet dolore magna aliquam erat volutpat. Ut wisi enim ad minim veniam, quis nostrud exerci tationmcorper suscipit lobortis nisl ut aliquip ex ea commodo consequat. Duis autem vel eum iriure dolor in hendrerit in vulputate velit esse molestie consequat, vel illum dolore eu feugiat nulla facilisis at vero eros et accumsan et iusto odio dignissim qui blandit praesent luptatum zzril delenit augue duis dolore te feugait nulla facilisi.</p>
    <p>Nam liber tempor cum soluta nobis eleifend option congue nihil imprdiet doming id quod mazim placerat facer possim assum. Typi non habent claritatem insitam;</p>
    <p>Est usus legentis in iis qui facit eorum claritatem.</p>
    <p>Investigationes demonstraverunt lectores legere me lius quod ii legunt saepius. Claritas est etiam processus dynamicus, qui sequitur mutationem consuetudium lectorum. Mirum est notare quam littera gothica, quam nunc putamus parum claram, anteposuerit litterarum formas humanitatis per seacula quarta decima et quinta decima. Eodem modo typi, qui nunc nobis videntur parum clari, fiant sollemnes in futurum.</p>
    <p>consectetuer adipiscing elit, sed diam nonummy nibh euismod tincidunt ut laoreet dolore magna aliquam erat volutpat. Ut wisi enim ad minim veniam, quis nostrud exerci tation ullamcorper suscipit lobortis nisl ut aliquip ex ea commodo consequat. Duis autem vel eum iriure dolor in hendrerit in vulputate velit esse molestie consequat, vel illum dolore eu feugiat nulla facilisis at vero eros et accumsan et iusto odio dignissim qui blandit praesent luptatum zzril delenit augue duis dolore te feugait nulla facilisi.</p>
    <p>Nam liber tempor cum soluta nobis eleifend option congue nihil imperdiet .</p>
  </article>

  <footer class="sign-off">
    <p class="sign-name">Advocate Karel Steenkamp</p>
    <p class="sign-details">KS Venture Frameworks (Pty) Ltd (Reg No.: 2019 / 374915 / 07)<br>LLB, LLM (Cum Laude), Cert.Dir (ABNQE), FCG (PTVRO)</p>
  </footer>

  <svg class="footer-bands" viewBox="0 0 855 70" aria-hidden="true">
    <rect x="0" y="13" width="855" height="32" fill="var(--band-dark)"/>
    <rect x="0" y="45" width="855" height="25" fill="var(--band-light)"/>
    <polygon points="529,13 543,0 557,13" fill="var(--brand-navy)"/>
    <polygon points="543,0 855,0 855,70 613,70" fill="var(--brand-blue)"/>
  </svg>
</main>
</body>
</html>
```